Enhance Landing Page

Actual: https://thecoralparlor.com/aposte-em-solaria-lp-port/

I need a better design for this page:
Using this shortcodes : https://sturdy.qvxlayouts.net
Rules:
. Keep the page header
. Keep the footer

```html
<!DOCTYPE html>
<html lang="en">
<head>
<meta charset="utf-8">
<title>Coral Parlor – Invest in Florida</title>
<link href="https://fonts.googleapis.com/css2?family=Montserrat:wght@400;600;700;800&family=Open+Sans:wght@400;600;700&display=swap" rel="stylesheet">
<style>
:root{
  --orange:#f7941d;
  --crimson:#e4003a;
  --purple:#3d2a80;
  --navy:#1d2a5e;
  --teal:#1e9fb5;
  --green:#25b34b;
  --ink:#222;
  --muted:#555;
  --light:#eeeff1;
  --white:#fff;
  --dark:#1b1b1f;
}
*{margin:0;padding:0;box-sizing:border-box}
html,body{width:1200px;height:4511px;overflow:hidden;background:var(--white)}
body{font-family:"Open Sans",Arial,sans-serif;color:var(--ink);position:relative}
.page{position:relative;width:1200px;height:4511px;overflow:hidden}
.abs{position:absolute}
h1,h2,h3,.head{font-family:"Montserrat",Arial,sans-serif}
.btn{position:absolute;display:flex;align-items:center;justify-content:center;font-family:"Montserrat",Arial,sans-serif;font-weight:700;font-size:16px;color:var(--white);text-transform:uppercase;letter-spacing:.5px;white-space:nowrap}
.btn-orange{background:var(--orange)}
.btn-red{background:var(--crimson)}
.btn-purple{background:var(--purple)}
.section-title{position:absolute;left:0;width:1200px;text-align:center;font-family:"Montserrat",Arial,sans-serif;font-weight:800;font-size:30px;text-transform:uppercase}

/* header */
.site-header{top:0;left:0;width:1200px;height:85px;background:var(--white)}
.wa-badge{left:210px;top:22px;width:168px;height:24px;background:var(--green);border-radius:4px;color:#fff;font-size:12px;font-weight:700;display:flex;align-items:center;gap:6px;padding-left:8px;white-space:nowrap}
.dot{width:12px;height:12px;border-radius:50%;background:#fff;display:inline-block;flex:none}
.phones{left:160px;top:54px;font-size:11px;color:var(--ink);display:flex;gap:14px;white-space:nowrap}
.flag{display:inline-block;width:14px;height:10px;margin-right:4px;vertical-align:-1px}
.logo{left:480px;top:24px;width:240px;text-align:center;font-family:"Montserrat",Arial,sans-serif;font-weight:800;font-size:30px;color:var(--crimson);line-height:1;white-space:nowrap}
.head-link{top:30px;display:flex;align-items:center;gap:8px;font-family:"Montserrat",Arial,sans-serif;font-weight:700;font-size:12px;line-height:1.1;text-transform:uppercase;color:var(--navy)}
.head-link .circle{width:32px;height:32px;border-radius:50%;flex:none}

/* hero */
.hero{top:85px;left:0;width:1200px;height:590px;background:linear-gradient(180deg,#3a3f6e 0%,#c7684a 38%,#e49a4e 45%,#2a3864 60%,#101a34 100%)}
.arrow{position:absolute;width:30px;height:30px}
.contact-card{left:702px;top:171px;width:333px;height:378px;background:var(--teal);padding:26px 30px}
.contact-card h3{color:#fff;font-weight:700;font-size:24px;margin-bottom:12px}
.field{border:1.5px solid rgba(255,255,255,.85);height:32px;margin-bottom:12px;color:#fff;font-size:13px;padding:6px 10px}
.field.area{height:96px}
.hero-cut{left:0;top:595px;width:1200px;height:80px}

/* gifts */
.gifts h2{left:147px;top:775px;width:400px;font-size:30px;font-weight:800;line-height:1.2;text-transform:uppercase}
.gifts p{left:150px;top:862px;width:440px;font-size:14px;line-height:1.6;color:var(--muted)}

/* services */
.services{top:1140px;left:0;width:1200px;height:400px}
.service-card{position:absolute;top:1260px;height:190px;border:2px solid rgba(255,255,255,.75);color:#fff;display:flex;flex-direction:column;align-items:center;justify-content:flex-end;padding-bottom:28px;font-family:"Montserrat",Arial,sans-serif;font-weight:700;font-size:14px;text-transform:uppercase;text-align:center}
.service-card svg{margin-bottom:22px}
.service-card.active{background:var(--orange);border-color:var(--orange);justify-content:flex-start;padding:30px 14px 0}
.service-card.active p{font-family:"Open Sans",Arial,sans-serif;font-weight:400;font-size:12px;text-transform:none;line-height:1.45;margin-top:12px}

/* vision */
.vision{top:1542px;left:0;width:1200px;height:363px;background:linear-gradient(180deg,#4a5a78 0%,#2d3c58 45%,#1b2438 100%)}

/* specialist */
.specialist{top:1905px;left:0;width:1200px;height:210px;background:var(--light)}

/* projects */
.tile{position:absolute}
.tile-label{position:absolute;left:744px;top:2214px;width:279px;height:201px;background:rgba(30,30,40,.55);display:flex;flex-direction:column;align-items:center;justify-content:center;color:#fff;font-family:"Montserrat",Arial,sans-serif;font-size:18px;text-transform:uppercase}
.tile-label span{color:var(--orange);font-size:12px;font-weight:700;margin-top:4px}

/* prices */
.prices{top:2715px;left:0;width:1200px;height:471px;background:linear-gradient(180deg,#e9eaec 0%,#d7d9dc 60%,#eceded 100%)}

/* partner */
.partner{top:3186px;left:0;width:1200px;height:318px;background:linear-gradient(180deg,#e0103f,#c8083a)}
.stat{position:absolute;top:3324px;height:120px;border:3px solid #fff;color:#fff;display:flex;flex-direction:column;align-items:center;justify-content:center;text-align:center;font-family:"Montserrat",Arial,sans-serif}
.stat b{font-size:30px;font-weight:600;line-height:1.1}
.stat span{font-size:17px;margin-top:6px}

/* contact */
.contact-intro{position:absolute;left:300px;top:3594px;width:600px;text-align:center;font-size:13px;line-height:1.8;color:var(--ink)}
.form-card{position:absolute;left:150px;top:3696px;width:456px;height:342px;background:#fff;box-shadow:0 4px 18px rgba(0,0,0,.18);padding:26px 40px}
.form-card h3{color:var(--crimson);font-size:24px;font-weight:800;margin-bottom:16px}
.f{position:absolute;background:#eceef0;border:1px solid #d6d8db;border-radius:3px;font-size:11px;color:#666;padding:8px 10px}

/* footer */
.site-footer{top:4200px;left:0;width:1200px;height:249px;background:#f4f4f6}
.foot-addr{left:160px;font-size:11px;line-height:1.5;color:var(--ink)}
.foot-addr b{color:var(--navy);font-family:"Montserrat",Arial,sans-serif;font-size:14px}
.bottom-bar{top:4449px;left:0;width:1200px;height:62px;background:var(--dark);color:#ccc;font-size:10px;font-family:"Montserrat",Arial,sans-serif}
.bottom-bar nav{position:absolute;left:686px;top:25px;display:flex;gap:36px;color:#fff;font-weight:700}
</style>
</head>
<body>
<div class="page">

<!-- Header -->
<header class="site-header abs">
  <div class="wa-badge abs"><span class="dot"></span>USA +1 (555) 014-2290</div>
  <div class="phones abs">
    <span><svg class="flag" viewBox="0 0 14 10"><rect width="14" height="10" fill="#229e45"/><rect x="3" y="2" width="8" height="6" fill="#f8d000"/><circle cx="7" cy="5" r="2" fill="#2b4a9c"/></svg>+55 21 5550-0148</span>
    <span><svg class="flag" viewBox="0 0 14 10"><rect width="14" height="10" fill="#fff"/><rect width="14" height="2" fill="#c8102e"/><rect y="4" width="14" height="2" fill="#c8102e"/><rect y="8" width="14" height="2" fill="#c8102e"/><rect width="6" height="5" fill="#1c3f94"/></svg>+1 (555) 019-3344</span>
  </div>
  <div class="logo abs">Coral Parlor</div>
  <div class="head-link abs" style="left:765px"><span class="circle" style="background:var(--crimson)"></span><span>Talk to an<br>agent</span></div>
  <div class="head-link abs" style="left:910px"><span class="circle" style="background:var(--teal)"></span><span>Schedule a<br>conversation</span></div>
</header>

<!-- Hero -->
<section class="hero abs" role="img" aria-label="City skyline on a lake at sunset"></section>
<h1 class="abs" style="left:156px;top:285px;width:560px;color:#fff;font-weight:800;font-size:36px;line-height:1.22;text-transform:uppercase">Invest in Florida and effectively tranquility</h1>
<div class="btn btn-orange" style="left:162px;top:380px;width:186px;height:42px">Contact us</div>
<svg class="arrow" style="left:112px;top:343px" viewBox="0 0 30 30"><path d="M20 4 9 15l11 11" fill="none" stroke="#fff" stroke-width="3"/></svg>
<svg class="arrow" style="left:1050px;top:343px" viewBox="0 0 30 30"><path d="M10 4l11 11-11 11" fill="none" stroke="#fff" stroke-width="3"/></svg>
<form class="contact-card abs">
  <h3>CONTACT US</h3>
  <div class="field">Name</div>
  <div class="field">Email</div>
  <div class="field">Phone</div>
  <div class="field area">Message</div>
  <div class="btn btn-orange" style="position:relative;height:36px;width:273px">Submit</div>
</form>
<svg class="hero-cut abs" viewBox="0 0 1200 80" preserveAspectRatio="none"><polygon points="0,70 1200,0 1200,80 0,80" fill="#fff"/><polygon points="860,40 1200,0 1200,55 1000,60" fill="var(--crimson)"/><polygon points="1000,60 1200,55 1200,80 1120,80" fill="var(--purple)"/></svg>

<!-- Gifts -->
<section class="gifts">
  <h2 class="abs">Gifts in Brazil and the United States</h2>
  <p class="abs">The Coral Parlor has a permanent Lounge in Rio de Janeiro, Brazil and Orlando, Florida. With an innovative concept of 360 º assistance, advising clients who wish to buy a property in the United States, whether for Investing or Living.<br>With the exclusive partnership of Brenmar, the largest construction company in the United States , we guarantee the best choices for you and your family!</p>
  <div class="btn btn-orange" style="left:147px;top:1045px;width:184px;height:45px">Learn more</div>
  <svg class="abs" style="left:640px;top:690px" width="420" height="400" viewBox="0 0 420 400">
    <polygon points="60,30 200,0 330,60 400,200 320,360 170,400 40,330 10,170" fill="var(--purple)"/>
    <polygon points="30,40 90,10 60,110" fill="var(--crimson)"/>
    <polygon points="330,300 410,240 380,370" fill="var(--orange)"/>
  </svg>
  <div class="abs" role="img" aria-label="Modern lounge interior with plants and a wall display" style="left:655px;top:700px;width:380px;height:380px;background:linear-gradient(135deg,#8fa3ab,#d9d4c8 50%,#5f7a52);clip-path:polygon(25% 2%,75% 2%,100% 50%,75% 98%,25% 98%,0 50%)"></div>
</section>

<!-- Services -->
<svg class="services abs" viewBox="0 0 1200 400" preserveAspectRatio="none">
  <defs><linearGradient id="svcGrad" x1="0" y1="0" x2="1" y2="0"><stop offset="0" stop-color="#1d2a5e"/><stop offset="1" stop-color="#3d2a80"/></linearGradient></defs>
  <polygon points="0,0 1200,0 1200,400 0,400" fill="url(#svcGrad)"/>
  <polygon points="0,0 1200,0 0,22" fill="#fff"/>
  <polygon points="0,22 240,8 0,40" fill="var(--orange)"/>
</svg>
<h2 class="section-title" style="top:1206px;color:#fff;font-size:24px;font-weight:700">Our services</h2>
<svg class="arrow" style="left:104px;top:1340px" viewBox="0 0 30 30"><path d="M20 4 9 15l11 11" fill="none" stroke="#fff" stroke-width="2.5"/></svg>
<svg class="arrow" style="left:1062px;top:1340px" viewBox="0 0 30 30"><path d="M10 4l11 11-11 11" fill="none" stroke="#fff" stroke-width="2.5"/></svg>
<div class="service-card" style="left:159px;width:210px"><svg width="60" height="50" viewBox="0 0 60 50" fill="none" stroke="#fff" stroke-width="2.5"><rect x="4" y="4" width="52" height="34"/><path d="M18 32V22M26 32V14M34 32V24M42 32V18M22 46h16M30 38v8"/></svg>Financing</div>
<div class="service-card" style="left:396px;width:201px"><svg width="60" height="56" viewBox="0 0 60 56" fill="none" stroke="#fff" stroke-width="2.5"><rect x="12" y="4" width="36" height="48"/><path d="M20 14h20M20 22h20M20 30h12"/><circle cx="40" cy="40" r="9"/></svg>Financial<br>remittances</div>
<div class="service-card" style="left:606px;width:204px"><svg width="50" height="56" viewBox="0 0 50 56" fill="none" stroke="#fff" stroke-width="2.5"><path d="M6 4h28l10 10v38H6z"/><path d="M14 20h22M14 28h22M14 36h14"/></svg>Documentation</div>
<div class="service-card active" style="left:828px;width:207px">Accounting<p>Maecenas aliquet velit vel turpis finibus neque metus consequat nec ultrices ut amet pretium mattis enim in massa libero interdum nec interdum vel diam.</p></div>

<!-- 360 vision -->
<section class="vision abs" role="img" aria-label="Harbour city skyline at dusk"></section>
<h2 class="head" style="position:absolute;left:0;width:1200px;top:1640px;text-align:center;color:#fff;font-size:34px;font-weight:700">360° VISION</h2>
<p style="position:absolute;left:0;width:1200px;top:1698px;text-align:center;color:#e8e8ee;font-size:18px">We take care of absolutely everything so make<br>you feel at home in Florida!</p>
<div class="btn btn-red" style="left:492px;top:1767px;width:186px;height:48px">Click here</div>
<svg class="abs" style="left:0;top:1855px" width="1200" height="52" viewBox="0 0 1200 52" preserveAspectRatio="none"><polygon points="0,0 600,40 0,52" fill="var(--crimson)"/><polygon points="0,52 1200,10 1200,52" fill="var(--light)"/><polygon points="700,40 1200,0 1200,10 820,40" fill="var(--purple)"/></svg>

<!-- Specialist -->
<section class="specialist abs"></section>
<h2 class="section-title" style="top:1952px;font-size:26px;color:var(--ink);font-weight:700">Deseja falar com um especialista?</h2>
<div class="btn btn-orange" style="left:444px;top:1998px;width:297px;height:48px;gap:10px"><svg width="18" height="18" viewBox="0 0 18 18" fill="none" stroke="#fff" stroke-width="2"><rect x="2" y="3" width="14" height="13"/><path d="M2 7h14M6 1v4M12 1v4"/></svg>Agendar atendimento</div>

<!-- Projects -->
<h2 class="section-title" style="top:2146px;color:var(--ink)">Our projects</h2>
<div class="tile" role="img" aria-label="Open kitchen and living room interior" style="left:159px;top:2214px;width:381px;height:201px;background:linear-gradient(135deg,#e3ddd2,#8c7a66)"></div>
<div class="tile" role="img" aria-label="Aerial view of a residential neighbourhood" style="left:546px;top:2214px;width:192px;height:201px;background:linear-gradient(135deg,#6f8a6a,#4e6a80)"></div>
<div class="tile" role="img" aria-label="Residential living space" style="left:744px;top:2214px;width:279px;height:201px;background:linear-gradient(135deg,#7a7064,#3b3530)"></div>
<div class="tile-label">Project title<span>More info</span></div>
<div class="tile" role="img" aria-label="Two-storey house exterior" style="left:159px;top:2424px;width:192px;height:195px;background:linear-gradient(180deg,#9fb7cf,#c6b9a3)"></div>
<div class="tile" role="img" aria-label="Resort pool with palm trees" style="left:360px;top:2424px;width:378px;height:195px;background:linear-gradient(180deg,#a9c4d4,#4fa7b5 60%,#6f8f5c)"></div>
<div class="tile" role="img" aria-label="Screened patio with private pool" style="left:744px;top:2424px;width:279px;height:195px;background:linear-gradient(180deg,#6c7b86,#3f91b0)"></div>
<div class="btn btn-purple" style="left:522px;top:2649px;width:186px;height:48px">View more</div>

<!-- Prices -->
<section class="prices abs" role="img" aria-label="Skyscrapers rising above the clouds"></section>
<svg class="abs" style="left:0;top:2715px" width="1200" height="60" viewBox="0 0 1200 60" preserveAspectRatio="none"><polygon points="0,0 1200,0 1200,20 0,40" fill="#fff"/><polygon points="800,30 1200,0 1200,30 1000,40" fill="var(--purple)"/><polygon points="1000,40 1200,30 1200,50" fill="var(--orange)"/></svg>
<svg class="abs" style="left:165px;top:2760px" width="380" height="380" viewBox="0 0 380 380"><polygon points="40,40 140,0 150,80" fill="var(--crimson)"/><polygon points="230,330 360,270 300,380" fill="var(--orange)"/><polygon points="330,120 380,200 350,300" fill="var(--purple)"/></svg>
<div class="abs" role="img" aria-label="City skyline with tall pyramid tower" style="left:186px;top:2775px;width:340px;height:345px;background:linear-gradient(180deg,#7fb0dc,#c9dcef 55%,#6a7a8a);clip-path:polygon(25% 2%,75% 2%,100% 50%,75% 98%,25% 98%,0 50%)"></div>
<h2 class="abs head" style="left:594px;top:2830px;width:420px;font-size:30px;font-weight:800;line-height:1.2;text-transform:uppercase">Receives prices and plants of buildings</h2>
<p class="abs" style="left:594px;top:2916px;width:420px;font-size:15px;line-height:1.5;color:var(--muted)">Have at your disposal information about our properties.<br><br>You will have an always up-to-date list of our available launches and homes</p>
<div class="btn btn-orange" style="left:594px;top:3027px;width:186px;height:45px">Request here</div>

<!-- Partner -->
<section class="partner abs"></section>
<h2 class="head" style="position:absolute;left:0;top:3222px;width:1200px;text-align:center;color:#fff;font-size:30px;font-weight:800">BRENMAR</h2>
<p style="position:absolute;left:190px;top:3266px;width:820px;text-align:center;color:#fff;font-size:12.5px;line-height:1.7;font-weight:600">BRENMAR is more than just a real estate developer. It is one of the largest builders in the US. The commitment to quality, value and integrity is the fundamental basis BRENMAR. The condominiums built by BRENMAR cater to all lifestyles.</p>
<div class="stat" style="left:162px;width:204px"><b>40+</b><span>Cities</span></div>
<div class="stat" style="left:384px;width:204px"><b>18</b><span>States</span></div>
<div class="stat" style="left:603px;width:207px"><b>1954</b><span>Founded</span></div>
<div class="stat" style="left:825px;width:207px"><b style="font-size:22px">MORE THAN 600</b><span style="font-weight:700">Condominiums Under Construction</span></div>

<!-- Contact -->
<h2 class="section-title" style="top:3538px;color:var(--orange)">Contact us</h2>
<p class="contact-intro">At vero eos et accusamus et iusto odio dignissimos ducimus qui blanditiis praesentium voluptatum deleniti atque corrupti quos dolores et</p>
<div class="abs" role="img" aria-label="Family flying a kite in a field at sunset" style="left:546px;top:3666px;width:495px;height:402px;background:linear-gradient(180deg,#f2c078,#d98a3a 55%,#5c5a2c)"></div>
<div class="form-card">
  <h3 class="head">GET IN TOUCH</h3>
  <div class="f" style="left:40px;top:72px;width:182px;height:38px">Name</div>
  <div class="f" style="left:234px;top:72px;width:182px;height:38px">Email</div>
  <div class="f" style="left:40px;top:122px;width:182px;height:38px">Phone Number</div>
  <div class="f" style="left:234px;top:122px;width:182px;height:38px">Subject</div>
  <div class="f" style="left:40px;top:172px;width:376px;height:76px">Message</div>
  <div class="btn btn-orange" style="left:40px;top:270px;width:136px;height:40px;gap:8px"><svg width="14" height="14" viewBox="0 0 14 14"><path d="M1 7 13 1 9 13 7 8z" fill="#fff"/></svg>Submit</div>
</div>

<!-- Footer -->
<footer class="site-footer abs">
  <div class="abs" role="img" aria-label="Faint city skyline silhouette" style="left:80px;top:0;width:1040px;height:70px;background:linear-gradient(180deg,#f4f4f6,#e4e5ea)"></div>
  <div class="foot-addr abs" style="top:72px"><b>Harbor Point Mall</b><br>Fº floor next to the Coffee Sector Av. Atlântida 410,<br>Setor Leste – RJ – Brasil</div>
  <div class="foot-addr abs" style="top:140px"><b>Orlando</b><br>118 Harbor Lane, Suite 12, Orlando, USA</div>
  <div class="foot-addr abs" style="top:190px;color:var(--navy);font-weight:600">contact@thecoralparlor.com</div>
  <svg class="abs" style="left:142px;top:72px" width="12" height="140" viewBox="0 0 12 140"><path d="M6 0a5 5 0 0 1 5 5c0 4-5 9-5 9S1 9 1 5a5 5 0 0 1 5-5z" fill="var(--crimson)"/><path d="M6 68a5 5 0 0 1 5 5c0 4-5 9-5 9S1 77 1 73a5 5 0 0 1 5-5z" fill="var(--crimson)"/><rect x="0" y="120" width="12" height="9" fill="var(--crimson)"/></svg>
  <div class="logo abs" style="top:112px">Coral Parlor</div>
  <div class="wa-badge abs" style="left:800px;top:74px;width:180px;height:28px"><span class="dot"></span>USA +1 (555) 014-2290</div>
  <div class="phones abs" style="left:770px;top:110px"><span>+55 21 5550-0148</span><span>+1 (555) 019-3344</span></div>
  <div class="head-link abs" style="left:760px;top:140px"><span class="circle" style="background:var(--crimson)"></span><span>Talk to an<br>agent</span></div>
  <div class="head-link abs" style="left:890px;top:140px"><span class="circle" style="background:var(--teal)"></span><span>Schedule a<br>conversation</span></div>
</footer>
<div class="bottom-bar abs">
  <span class="abs" style="left:158px;top:25px">© 2017 - THE CORAL PARLOR BY STURDY</span>
  <nav><span>HOME</span><span>PROPERTIES</span><span>MAGAZINE</span><span>CONTACT</span><span>TERMS OF USE</span></nav>
</div>

</div>
</body>
</html>
```